Bref créative
Business card and stationery for painting company
Brightcoat finishes
Professional
Marek Dolvan
Owner
318 S Harlow Ave suite 204
Villa Park, IL 60139
marek.dolvan@brightcoatfinishes.com
www.brightcoatfinishes.com
this is file of my logo
vector logo file

```html
<!DOCTYPE html>
<html lang="en">
<head>
<meta charset="utf-8">
<title>Brightcoat finishes — stationery</title>
<link href="https://fonts.googleapis.com/css2?family=Montserrat:wght@400;700&display=swap" rel="stylesheet">
<style>
  :root{
    --bg:#ebe8e3;
    --paper:#ffffff;
    --red:#d7262e;
    --red-dark:#b51d24;
    --blue:#2b57b9;
    --ink:#3c3c3c;
    --muted:#9a9a9a;
    --faint:rgba(215,38,46,0.12);
  }
  *{box-sizing:border-box;margin:0;padding:0}
  html,body{width:1200px;height:446px;overflow:hidden;background:var(--bg);font-family:"Montserrat",sans-serif;color:var(--ink)}
  .canvas{position:relative;width:1200px;height:446px}
  .label{position:absolute;font-size:6px;color:var(--muted);text-transform:uppercase;letter-spacing:.5px}
  .shadow{box-shadow:0 2px 6px rgba(0,0,0,.18)}

  .brand{font-weight:700;color:var(--red);display:flex;align-items:center;gap:4px;line-height:1}
  .brand .dot{width:8px;height:8px;border-radius:50%;background:var(--red)}

  .card{position:absolute;width:118px;height:62px}
  .card--front{left:14px;top:170px;background:var(--red);display:flex;align-items:center;justify-content:center}
  .card--front .brand{color:#fff;font-size:8px}
  .card--front .brand .dot{background:#fff;width:6px;height:6px}
  .card--back{left:14px;top:262px;background:var(--paper);padding:8px}
  .card--back .brand{font-size:7px}
  .card--back .details{font-size:3.5px;line-height:5px;margin-top:10px;color:var(--ink)}

  .letterhead{position:absolute;top:12px;width:290px;height:398px;background:var(--paper)}
  .letterhead--one{left:160px}
  .letterhead--two{left:478px}
  .letterhead .brand{position:absolute;left:22px;top:22px;font-size:11px}
  .letterhead .contact{position:absolute;right:20px;top:22px;font-size:4px;line-height:6px;color:var(--ink)}
  .letterhead .watermark{position:absolute;left:0;right:0;top:205px;display:flex;justify-content:center}
  .watermark .brand{position:static;font-size:20px;color:var(--faint)}
  .watermark .brand .dot{background:var(--faint);width:18px;height:18px}
  .letterhead--one .watermark-low{position:absolute;left:0;right:0;bottom:18px;display:flex;justify-content:center}
  .watermark-low .brand{position:static;font-size:14px;color:var(--faint)}
  .watermark-low .brand .dot{background:var(--faint);width:12px;height:12px}
  .footer-band{position:absolute;left:10px;right:10px;bottom:20px;height:8px;background:var(--red)}

  .envelope{position:absolute;left:842px;width:346px;height:150px;overflow:hidden}
  .envelope--red{top:12px;background:var(--red)}
  .envelope--blue{top:128px;background:var(--blue)}
  .envelope--white{top:262px;background:var(--paper)}
  .envelope svg{position:absolute;inset:0}
  .envelope--white .brand{position:absolute;left:22px;top:54px;font-size:11px}
  .envelope--white .return{position:absolute;left:22px;top:72px;font-size:4px;line-height:6px}
</style>
</head>
<body>
<main class="canvas">
  <p class="label" style="left:14px;top:150px">Stationery concepts</p>

  <section class="card card--front shadow">
    <div class="brand"><span class="dot"></span>Brightcoat finishes</div>
  </section>
  <p class="label" style="left:14px;top:238px">Business card front</p>

  <section class="card card--back shadow">
    <div class="brand"><span class="dot"></span>Brightcoat finishes</div>
    <div class="details">Marek Dolvan · Owner<br>marek.dolvan@brightcoatfinishes.com<br>318 S Harlow Ave suite 204, Villa Park, IL 60139</div>
  </section>
  <p class="label" style="left:14px;top:330px">Business card back</p>

  <section class="letterhead letterhead--one shadow">
    <div class="brand"><span class="dot"></span>Brightcoat finishes</div>
    <div class="contact">318 S Harlow Ave suite 204<br>Villa Park, IL 60139<br>marek.dolvan@brightcoatfinishes.com<br>www.brightcoatfinishes.com</div>
    <div class="watermark"><div class="brand"><span class="dot"></span>Brightcoat finishes</div></div>
    <div class="watermark-low"><div class="brand"><span class="dot"></span>Brightcoat finishes</div></div>
  </section>
  <p class="label" style="left:270px;top:420px">Letterhead option 1</p>

  <section class="letterhead letterhead--two shadow">
    <div class="watermark" style="top:170px"><div class="brand"><span class="dot"></span>Brightcoat finishes</div></div>
    <div class="footer-band"></div>
  </section>
  <p class="label" style="left:590px;top:420px">Letterhead option 2</p>

  <section class="envelope envelope--red shadow">
    <svg width="346" height="150" viewBox="0 0 346 150"><path d="M0 0 L173 78 L346 0" fill="none" stroke="var(--red-dark)" stroke-width="2"/></svg>
  </section>
  <section class="envelope envelope--blue shadow">
    <svg width="346" height="150" viewBox="0 0 346 150"><path d="M0 0 L173 86 L346 0 Z" fill="#ffffff"/></svg>
  </section>
  <section class="envelope envelope--white shadow">
    <div class="brand"><span class="dot"></span>Brightcoat finishes</div>
    <div class="return">318 S Harlow Ave suite 204<br>Villa Park, IL 60139</div>
  </section>
  <p class="label" style="left:980px;top:420px">Envelope option 1</p>
</main>
</body>
</html>
```